Ashford Church of Grace (this will be used for new church sign) sign will be 4'x8' and would like also listed Sunday School 9:00am Worship Service 10:30am.

Logo Text

ASHFORD CHURCH OF GRACE

```html
<!DOCTYPE html>
<html lang="en">
<head>
<meta charset="utf-8">
<title>Ashford Church of Grace – Service Times Sign</title>
<link rel="stylesheet" href="https://fonts.googleapis.com/css2?family=Open+Sans:wght@400;800&family=Oswald:wght@700&display=swap">
<style>
  :root {
    --brand-blue: #2075bc;
    --ink: #000000;
    --paper: #ffffff;
  }
  html, body {
    margin: 0;
    padding: 0;
    width: 1200px;
    height: 1200px;
    overflow: hidden;
    background: var(--paper);
  }
  .sign-canvas {
    display: block;
    width: 1200px;
    height: 1200px;
  }
  .sign-frame { fill: var(--paper); stroke: var(--ink); stroke-width: 1.6; }
  .header-band { fill: var(--brand-blue); }
  .church-name {
    font-family: "Open Sans", Arial, sans-serif;
    font-weight: 800;
    font-size: 172px;
    fill: var(--paper);
  }
  .church-tagline {
    font-family: "Open Sans", Arial, sans-serif;
    font-weight: 400;
    font-size: 54px;
    letter-spacing: 5px;
    fill: var(--paper);
  }
  .tagline-rule { fill: var(--paper); }
  .schedule-line {
    font-family: "Oswald", "Arial Narrow", sans-serif;
    font-weight: 700;
    font-size: 90px;
    fill: var(--ink);
  }
  .schedule-divider { fill: var(--brand-blue); }
</style>
</head>
<body>
<svg class="sign-canvas" viewBox="0 0 1200 1200" xmlns="http://www.w3.org/2000/svg" role="img" aria-label="Ashford Church of Grace sign: Sunday School 9:00 AM, Worship Service 10:30 AM">
  <rect class="sign-frame" x="21.7" y="308.7" width="1157" height="580"/>
  <rect class="header-band" x="22.5" y="309.5" width="1155.5" height="288.5"/>

  <text class="church-name" x="600" y="476" text-anchor="middle">ASHFORD</text>

  <polygon class="tagline-rule" points="47,548 285,544 285,551.5"/>
  <text class="church-tagline" x="603" y="567" text-anchor="middle">CHURCH OF GRACE</text>
  <polygon class="tagline-rule" points="920,542.5 1148,546 920,550"/>

  <text class="schedule-line" x="625.5" y="707" text-anchor="middle" textLength="873" lengthAdjust="spacingAndGlyphs">SUNDAY SCHOOL 9:00 AM</text>

  <polygon class="schedule-divider" points="323,746.5 566,742.5 566,750"/>
  <polygon class="schedule-divider" points="635,742.5 877,746.5 635,750"/>

  <text class="schedule-line" x="601" y="851" text-anchor="middle" textLength="1048" lengthAdjust="spacingAndGlyphs">WORSHIP SERVICE 10:30 AM</text>
</svg>
</body>
</html>
```